Contractor Plan "B"/Getting Screwed?/Something Useful

We are sending out a series of postcards to a group of local contractors.

The first in the series is: Plan B: Pink Bubble Wrap. Plan A is to buy insurance from my agency. This will be printed, front and back on card stock. We will then glue a piece of bubble wrap to the card and place it in an envelope for delivery.

The second card will be along the same lines but will ask if the client is getting screwed by his current Insurance Company. We will glue a screw in the middle of the card and place the card in an envelope for delivery. On the bottom of we might tell them to call us to get unscrewed.

The third card will follow those lines but say something like: We sent you bubble wrap for your Plan B and you didn't call. Then we sent you something funny but you didn't call. We decided to send you something useful so you might call now! With this card, we are going to send a carpenter pencil.

I am attaching a rough outline of my sketch design for the first card so you will have basic information we will need such as phone number and coverages we offer. If you feel like there is too much info for the size of the card, we can leave some off. I just want the phone to ring! Also, feel free to adjust the wording to make it work better...creative design is not my strong suit!!

I would like for all three cards to be designed. Each can have the same backside. Also, please keep in mind, this is not a postcard so you don't have to leave the blanks on the back for addressing. Each will be mailed in an envelope.

I have also uploaded my logo file as we have recently redone the logo.
Updates

Here is more guidance on the project: The cards are going to be 10 cm wide and 23 cm tall. I have added more wording in the brief. Also, I attached a word doc with a good idea of what to use for wording. Basically I want the following idea: Card 1: At top of card - Plan B: Pink Bubble Wrap Below the bubble wrap - Plan A: Call us so you don't have to use Pink Bubble Wrap Card 2: At top of card - Getting Screwed? Is your current agent taking you for granted? Below the area where we are going to glue a screw - Get unscrewed, Call us! Card 3: At top of card - We have the sharpest pencil in town! We will leave space for a carpenter pencil to be attached tot he card. On the other side of the open space - Call us today for the best rates on your insurance!

Please review the attached word doc for an idea of what to put on the back of the card. To be clear, we need three designs for the front of the card and can probably use just one design for the back of all three. If you think we need to have a different design for the back of each, I would like to see your ideas. Thank you for your hard work on these!

Reason: Hi, I am extending the time as I am expecting a few more submissions. Thank you!

Target Market(s)

We are targeting both contractors and truckers with this campaign.

Industry/Entity Type

Insurance

Requirements
Must have
• Clever wording. It needs to be a call to action and doesn't need to have too many specifics.

We also have to have space in the middle to glue the bubble wrap on the first card, the screw in the second and attach the pencil in the third.

```html
<!DOCTYPE html>
<html lang="en">
<head>
<meta charset="utf-8">
<title>Plan B – Pink Bubble Wrap</title>
<link rel="stylesheet" href="https://fonts.googleapis.com/css2?family=Signika:wght@400;500;600&family=Lobster+Two:ital,wght@1,700&display=swap">
<style>
  :root {
    --ink: #262626;
    --pink: #e6338c;
    --sky-top: #eef0dc;
    --sky-mid: #e3e7d2;
    --sky-low: #c9cfc4;
    --cream: #f6f3df;
    --brand: #b3262e;
    --bubble-light: #fbe2ee;
    --bubble-deep: #e889b6;
    --figure: #3a3d44;
  }
  html, body {
    margin: 0;
    padding: 0;
    width: 1200px;
    height: 2759px;
    overflow: hidden;
  }
  .card {
    position: relative;
    width: 1200px;
    height: 2759px;
    overflow: hidden;
    font-family: "Signika", sans-serif;
    color: var(--ink);
  }
  .sky-scene {
    position: absolute;
    inset: 0 0 179px 0;
    display: block;
  }
  .headline {
    position: absolute;
    left: 0;
    width: 100%;
    text-align: center;
    margin: 0;
  }
  .headline-kicker {
    top: 48px;
    font-size: 56px;
    font-weight: 600;
    line-height: 1;
  }
  .headline-main {
    top: 138px;
    font-size: 74px;
    font-weight: 500;
    line-height: 1;
  }
  .headline-product {
    top: 262px;
    font-family: "Lobster Two", cursive;
    font-style: italic;
    font-weight: 700;
    font-size: 118px;
    line-height: 1;
    color: var(--pink);
  }
  .call-line {
    position: absolute;
    top: 2262px;
    width: 100%;
    text-align: center;
    font-size: 70px;
    font-weight: 500;
    line-height: 1;
  }
  .call-line .accent { color: var(--pink); }
  .phone {
    position: absolute;
    top: 2350px;
    width: 100%;
    text-align: center;
    font-size: 120px;
    font-weight: 400;
    line-height: 1;
    letter-spacing: 2px;
  }
  .tagline {
    position: absolute;
    top: 2518px;
    width: 100%;
    text-align: center;
    font-size: 35px;
    font-weight: 400;
    line-height: 1;
  }
  .brand-band {
    position: absolute;
    left: 0;
    bottom: 0;
    width: 100%;
    height: 179px;
    background: var(--cream);
    display: flex;
    align-items: center;
    justify-content: center;
    gap: 24px;
  }
  .brand-mark {
    width: 46px;
    height: 46px;
    background: var(--brand);
  }
  .brand-name {
    font-family: "Signika", sans-serif;
    font-weight: 600;
    font-size: 66px;
    color: var(--brand);
    line-height: 1;
  }
</style>
</head>
<body>
<main class="card">
  <svg class="sky-scene" width="1200" height="2580" viewBox="0 0 1200 2580" xmlns="http://www.w3.org/2000/svg">
    <defs>
      <linearGradient id="skyFill" x1="0" y1="0" x2="0" y2="1">
        <stop offset="0" stop-color="var(--sky-top)"/>
        <stop offset="0.6" stop-color="var(--sky-mid)"/>
        <stop offset="1" stop-color="var(--sky-low)"/>
      </linearGradient>
      <radialGradient id="bubbleFill" cx="0.45" cy="0.4" r="0.6">
        <stop offset="0" stop-color="var(--bubble-light)"/>
        <stop offset="1" stop-color="var(--bubble-deep)"/>
      </radialGradient>
    </defs>
    <rect width="1200" height="2580" fill="url(#skyFill)" role="img" aria-label="Soft cloudy pale green sky"/>
    <line class="light-streak" x1="1058" y1="985" x2="1200" y2="945" stroke="#ffffff" stroke-width="30" stroke-linecap="round"/>

    <rect x="535" y="400" width="240" height="520" rx="40" fill="var(--figure)" opacity="0.35" role="img" aria-label="Businessman in a dark suit standing on top of the bubble, reaching upward"/>
    <circle cx="690" cy="1310" r="437" fill="url(#bubbleFill)" opacity="0.85" role="img" aria-label="Large pink bubble enclosing a city skyline on pink clouds"/>

    <rect x="335" y="1690" width="136" height="205" rx="30" fill="var(--figure)" opacity="0.3" role="img" aria-label="Businesswoman sitting cross-legged on top of a bubble"/>
    <circle cx="395" cy="2080" r="195" fill="url(#bubbleFill)" opacity="0.9" role="img" aria-label="Pink bubble enclosing a money bag"/>

    <rect x="985" y="1885" width="150" height="225" rx="30" fill="var(--figure)" opacity="0.3" role="img" aria-label="Businessman balancing on top of a small bubble"/>
    <circle cx="1046" cy="2218" r="133" fill="url(#bubbleFill)" opacity="0.85" role="img" aria-label="Small pink bubble enclosing a stack of binders"/>
  </svg>

  <h2 class="headline headline-kicker">Plan B</h2>
  <h1 class="headline headline-main">Protect your business with</h1>
  <p class="headline headline-product">Pink Bubble Wrap</p>

  <p class="call-line" style="margin:0">Call us to avoid <span class="accent">Plan B</span></p>
  <p class="phone" style="margin:0">555-014-2287</p>
  <p class="tagline" style="margin:0">Why pink?&nbsp; You might not get sued if they think you are a wuss.</p>

  <footer class="brand-band">
    <span class="brand-mark"></span>
    <span class="brand-name">Harbor Lane Insurance</span>
  </footer>
</main>
</body>
</html>
```